Veterinary Power Point Template/Master

Dear Creatives,
we would need a Power Point Template that can be used for internal and external presentations. It'll mostly be needed to create B2B presentations at congresses or seminars, at which our vets attend as podium guests and lecturers.

What is important?
We see ourselves as highly professional, clean and innovative. One of our greatest mission is to build our work on latest medical research and the latest technology within veterinary medicine.
Therefore, our design should represent exactly this and look modern, professional and clinical.

Which slides do we need? What should they include?
- title
- section slides
- agenda
- Team slides to introduce our personell
- classic title & content
- slides to include different media and text options
- page numbers
- date
- our logo
- icons (if possible)

Unfortunately, we do not have an english version of our website yet, but feel free to browse through it to get a feeling for our appearance and values: https://www.tierpraxolan.at

We will also attach our little brand booklet as a guidance for you. BUT feel free to think out of the box and create a beautiful PPT design which is fun to watch.

Thrilled to see your great work already!

Target Market(s)

Austria

Industry/Entity Type

veterinary medicine

Font styles to use
Sans Serif
Other font styles liked:
• please only use Roboto font

Requirements
Must have
• items described in the creative brief
Nice to have
• animations and fancy transitions
Should not have
• Comic Sans or classic PPT Preset Designs

```html
<!DOCTYPE html>
<html lang="en">
<head>
<meta charset="utf-8">
<title>Tierpraxolan – Presentation Template</title>
<link rel="stylesheet" href="https://fonts.googleapis.com/css2?family=Poppins:wght@600;700;800&family=Roboto:wght@400;500;700&display=swap">
<style>
:root{
  --navy:#243447;
  --gold:#d4a017;
  --gold-deep:#c99a12;
  --green:#1aa57a;
  --rust:#bf531c;
  --ink:#3b3b3b;
  --muted:#6b6f75;
  --white:#ffffff;
  --paper:#ffffff;
}
*{box-sizing:border-box;margin:0;padding:0}
html,body{width:1200px;height:2194px;overflow:hidden;background:var(--paper)}
body{position:relative;font-family:"Roboto",sans-serif;color:var(--ink)}
.defs{position:absolute;width:0;height:0}
.slide{position:absolute;width:542px;height:304px;overflow:hidden;background:var(--white);box-shadow:4px 6px 14px rgba(0,0,0,.28)}
.slide > svg.shapes{position:absolute;left:0;top:0;width:542px;height:304px}
.col-l{left:37px}.col-r{left:622px}
.r1{top:79px}.r2{top:426px}.r3{top:773px}.r4{top:1119px}.r5{top:1465px}.r6{top:1811px}
.abs{position:absolute}
.brand{position:absolute;display:flex;align-items:center;gap:5px}
.brand-dot{width:26px;height:26px;border-radius:50%;background:var(--navy);border:2px solid var(--gold)}
.brand-name{font-family:"Roboto",sans-serif;font-weight:700;font-size:10.5px;color:var(--navy);line-height:1}
.brand-tag{font-size:3.6px;color:var(--gold);margin-top:1px;letter-spacing:.1px}
.brand.on-dark .brand-name{color:var(--white)}
.brand.on-dark .brand-dot{background:var(--white)}
.footer-copy{position:absolute;left:42px;bottom:9px;font-size:5px;color:var(--ink)}
.footer-page{position:absolute;right:40px;bottom:9px;font-size:5px;color:var(--ink)}
.on-navy .footer-copy,.on-navy .footer-page,.gold-foot{color:var(--gold)}
.display{font-family:"Poppins",sans-serif;font-weight:800;color:var(--navy);line-height:1.22}
.body-copy{font-size:5.6px;line-height:1.45;text-align:justify;color:var(--ink)}
.eyebrow{font-size:5px;letter-spacing:1.2px;color:var(--ink)}
/* slide 1 */
.title-hero{left:290px;top:156px;font-size:19.5px;color:var(--white);line-height:1.4}
.title-sub{left:290px;top:210px;font-size:8.5px;color:var(--white);letter-spacing:-.2px}
.hero-brand{left:288px;top:96px}
.hero-brand .brand-dot{width:46px;height:46px;background:var(--white);border:3px solid var(--navy)}
.hero-brand .brand-name{font-size:17px;color:var(--navy)}
.hero-brand .brand-tag{font-size:6.5px;color:var(--white)}
/* agenda */
.agenda-item{position:absolute;display:flex;align-items:center;gap:12px;font-size:5.6px;color:var(--ink)}
.agenda-num{width:18px;height:18px;border-radius:50%;border:1.3px solid var(--gold);border-right-color:transparent;display:flex;align-items:center;justify-content:center;font-size:7px;color:var(--gold);font-weight:500}
/* pills */
.pill{position:absolute;border-radius:14px;color:var(--white);font-size:6.2px;line-height:1.2;text-align:center;padding:5px 8px}
/* bullets */
.bullet{position:absolute;left:318px;width:176px}
.bullet h4{font-size:7.5px;font-weight:700;color:var(--navy);margin-bottom:3px}
.bullet p{font-size:5.2px;line-height:1.55;color:var(--muted)}
.bullet-icon{position:absolute;left:272px;width:34px;height:34px;border-radius:50%;display:flex;align-items:center;justify-content:center}
/* team */
.member{position:absolute;width:96px;text-align:center}
.member svg{display:block;margin:0 auto}
.member .name{font-size:6.6px;color:var(--ink);margin-top:1px}
.member .role{font-size:3.4px;color:var(--ink);line-height:1.2}
/* testimonials */
.quote{position:absolute;width:136px;text-align:center}
.quote p{font-size:6.1px;line-height:1.3;color:var(--muted);text-align:justify;margin-top:10px}
.quote .who{font-size:6px;font-weight:700;letter-spacing:1.6px;color:var(--navy);margin-top:9px}
/* classic */
.col-head{font-size:7.5px;font-weight:700;color:var(--ink)}
.col-text{font-size:7.4px;line-height:1.36;text-align:justify;color:var(--ink)}
</style>
</head>
<body>

<svg class="defs" aria-hidden="true">
  <defs>
    <linearGradient id="gPortraitWarm" x1="0" y1="0" x2="1" y2="1"><stop offset="0" stop-color="#e9e6e2"/><stop offset=".55" stop-color="#b9aa98"/><stop offset="1" stop-color="#6f625a"/></linearGradient>
    <linearGradient id="gClinicBright" x1="0" y1="0" x2="1" y2="1"><stop offset="0" stop-color="#f3f4f6"/><stop offset=".6" stop-color="#cfd6de"/><stop offset="1" stop-color="#8a95a3"/></linearGradient>
    <linearGradient id="gMono" x1="0" y1="0" x2="1" y2="1"><stop offset="0" stop-color="#f1f1f1"/><stop offset=".6" stop-color="#9d9d9d"/><stop offset="1" stop-color="#2d2d2d"/></linearGradient>
    <linearGradient id="gMeadow" x1="0" y1="0" x2="0" y2="1"><stop offset="0" stop-color="#6fa6dc"/><stop offset=".45" stop-color="#c9d9ea"/><stop offset=".62" stop-color="#6a5646"/><stop offset="1" stop-color="#c8331f"/></linearGradient>
    <linearGradient id="gXray" x1="0" y1="0" x2="1" y2="1"><stop offset="0" stop-color="#1a1a1a"/><stop offset=".5" stop-color="#7c7c7c"/><stop offset="1" stop-color="#202020"/></linearGradient>
    <linearGradient id="gSurgery" x1="0" y1="0" x2="1" y2="1"><stop offset="0" stop-color="#d6dbe0"/><stop offset=".55" stop-color="#8d9aa6"/><stop offset="1" stop-color="#2f66b6"/></linearGradient>
    <linearGradient id="gGroup" x1="0" y1="0" x2="1" y2="1"><stop offset="0" stop-color="#c7c3bd"/><stop offset=".6" stop-color="#8b8fa3"/><stop offset="1" stop-color="#5a6a8c"/></linearGradient>
    <linearGradient id="gDinner" x1="0" y1="0" x2="1" y2="1"><stop offset="0" stop-color="#9c6a4a"/><stop offset=".5" stop-color="#d1a582"/><stop offset="1" stop-color="#efe6da"/></linearGradient>
    <linearGradient id="gWhiteDog" x1="0" y1="0" x2="1" y2="1"><stop offset="0" stop-color="#e8eef0"/><stop offset=".6" stop-color="#c9c9c0"/><stop offset="1" stop-color="#3f9c93"/></linearGradient>
    <linearGradient id="gScanner" x1="0" y1="0" x2="1" y2="1"><stop offset="0" stop-color="#d8e0e8"/><stop offset=".55" stop-color="#8b97a6"/><stop offset="1" stop-color="#4a3e38"/></linearGradient>
    <linearGradient id="gUltrasound" x1="0" y1="0" x2="1" y2="1"><stop offset="0" stop-color="#5f6b78"/><stop offset="1" stop-color="#c2b7ab"/></linearGradient>
    <linearGradient id="gPortraitSoft" x1="0" y1="0" x2="1" y2="1"><stop offset="0" stop-color="#e4e7ea"/><stop offset=".6" stop-color="#b3aa9f"/><stop offset="1" stop-color="#7d8794"/></linearGradient>
    <linearGradient id="gStaff" x1="0" y1="0" x2="0" y2="1"><stop offset="0" stop-color="#f2f2f2"/><stop offset=".55" stop-color="#b6b6b6"/><stop offset="1" stop-color="#1f1f1f"/></linearGradient>
  </defs>
</svg>

<!-- 1 Title -->
<section class="slide col-l r1 on-navy">
  <svg class="shapes" viewBox="0 0 542 304" aria-hidden="true">
    <rect width="542" height="304" fill="var(--gold)"/>
    <path d="M0 200 C150 215 320 228 420 205 S520 172 542 166 L542 304 L0 304 Z" fill="var(--navy)"/>
  </svg>
  <svg class="shapes" viewBox="0 0 542 304">
    <circle cx="134" cy="151" r="98" fill="url(#gPortraitWarm)" role="img" aria-label="Photo: veterinarian holding a small dog"/>
    <circle cx="134" cy="151" r="111" fill="none" stroke="var(--green)" stroke-width="4.5" stroke-linecap="round" pathLength="100" stroke-dasharray="30 70" transform="rotate(150 134 151)"/>
    <circle cx="134" cy="151" r="111" fill="none" stroke="var(--rust)" stroke-width="4.5" stroke-linecap="round" pathLength="100" stroke-dasharray="42 58" transform="rotate(-32 134 151)"/>
  </svg>
  <div class="brand hero-brand"><span class="brand-dot"></span><div><div class="brand-name">Tierpraxolan</div><div class="brand-tag">Fachklinik für Kleintiere</div></div></div>
  <h1 class="abs display title-hero">Place here your<br>Title Presentation</h1>
  <p class="abs title-sub">Your subtitle title presentation here</p>
  <p class="abs gold-foot" style="left:235px;bottom:9px;font-size:7px">© 2023 Tierpraxolan.</p>
</section>

<!-- 2 Agenda -->
<section class="slide col-r r1">
  <svg class="shapes" viewBox="0 0 542 304">
    <rect x="0" y="61" width="290" height="184" fill="var(--navy)"/>
    <circle cx="268" cy="153" r="91" fill="url(#gClinicBright)" role="img" aria-label="Photo: veterinarian in a bright treatment room"/>
    <circle cx="268" cy="153" r="100" fill="none" stroke="var(--green)" stroke-width="4.5" stroke-linecap="round" pathLength="100" stroke-dasharray="27 73" transform="rotate(110 268 153)"/>
  </svg>
  <div class="brand" style="left:38px;top:16px"><span class="brand-dot"></span><div><div class="brand-name">Tierpraxolan</div><div class="brand-tag">Fachklinik für Kleintiere</div></div></div>
  <p class="abs" style="left:44px;top:91px;font-family:Poppins,sans-serif;font-weight:700;font-size:5.4px;color:var(--white);letter-spacing:.5px">March 2023</p>
  <h2 class="abs display" style="left:44px;top:101px;font-size:12.5px;color:var(--white);line-height:1.5">Today<br>Agenda</h2>
  <p class="abs" style="left:44px;top:160px;font-family:Poppins,sans-serif;font-weight:700;font-size:7.2px;color:var(--white);line-height:1.5">Presenter<br>Dr. Lukas Brenner</p>
  <p class="abs" style="left:44px;top:184px;font-size:5.5px;color:var(--white);line-height:1.25">Chief executive officer,<br>Co-Founder</p>
  <div class="agenda-item" style="left:311px;top:50px"><span class="agenda-num">1</span>Lorem ipsum is simply dummy</div>
  <div class="agenda-item" style="left:349px;top:89px"><span class="agenda-num">2</span>Lorem ipsum is simply dummy</div>
  <div class="agenda-item" style="left:367px;top:128px"><span class="agenda-num">3</span>Lorem ipsum is simply dummy</div>
  <div class="agenda-item" style="left:367px;top:167px"><span class="agenda-num">4</span>Lorem ipsum is simply dummy</div>
  <div class="agenda-item" style="left:349px;top:207px"><span class="agenda-num">5</span>Lorem ipsum is simply dummy</div>
  <div class="agenda-item" style="left:311px;top:247px"><span class="agenda-num">6</span>Lorem ipsum is simply dummy</div>
  <p class="footer-copy">© 2023 Tierpraxolan.</p><p class="footer-page">| 2</p>
</section>

<!-- 3 Welcome -->
<section class="slide col-l r2 on-navy">
  <svg class="shapes" viewBox="0 0 542 304">
    <path d="M0 270 C120 262 300 282 420 272 S520 262 542 258 L542 304 L0 304 Z" fill="var(--navy)"/>
    <circle cx="398" cy="152" r="98" fill="url(#gMono)" role="img" aria-label="Black and white portrait of the clinic director"/>
    <circle cx="398" cy="152" r="110" fill="none" stroke="var(--gold)" stroke-width="4.5" stroke-linecap="round" pathLength="100" stroke-dasharray="32 68" transform="rotate(160 398 152)"/>
    <circle cx="398" cy="152" r="110" fill="none" stroke="var(--navy)" stroke-width="4.5" stroke-linecap="round" pathLength="100" stroke-dasharray="20 80" transform="rotate(-25 398 152)"/>
  </svg>
  <div class="brand" style="left:38px;top:16px"><span class="brand-dot"></span><div><div class="brand-name">Tierpraxolan</div><div class="brand-tag">Fachklinik für Kleintiere</div></div></div>
  <h2 class="abs display" style="left:38px;top:66px;font-size:13px">Welcome Message</h2>
  <p class="abs body-copy" style="left:40px;top:92px;width:222px">Lorem Ipsum is simply dummy text of the printing and typesetting industry. Lorem Ipsum has been the industry's standard dummy text ever since the 1500s, when an unknown printer took a galley of type and scrambled it to make a type specimen book. It has survived not only five centuries, but also the leap into electronic typesetting, remaining essentially unchanged. It was popularized in the 1960s with the release of Lettrafix sheets containing Lorem Ipsum passages, and more recently with desktop publishing software like Folio PageSetter including versions of Lorem Ipsum. It is a long-established fact that a reader will be distracted by the readable content of a page when looking at its layout. The point of using Lorem Ipsum is that it has a more-or-less normal distribution of letters, as</p>
  <p class="abs" style="left:41px;top:219px;font-family:Poppins,sans-serif;font-weight:700;font-size:8px;color:var(--ink)">Dr. Lukas Brenner</p>
  <p class="abs" style="left:41px;top:231px;font-size:6.6px;line-height:1.3;color:var(--ink)">Diplomate ECVS, Spezialist für Chirurgie Klinikleiter,<br>Geschäftsführer Jonas Weber</p>
  <p class="footer-copy">© 2023 Tierpraxolan.</p><p class="footer-page">| 3</p>
</section>

<!-- 4 Mission -->
<section class="slide col-r r2">
  <svg class="shapes" viewBox="0 0 542 304">
    <circle cx="414" cy="137" r="136" fill="url(#gMeadow)" role="img" aria-label="Photo: dog leaping through a field of red poppies"/>
    <circle cx="414" cy="137" r="148" fill="none" stroke="var(--gold)" stroke-width="4.5" stroke-linecap="round" pathLength="100" stroke-dasharray="30 70" transform="rotate(95 414 137)"/>
  </svg>
  <div class="brand" style="left:38px;top:16px"><span class="brand-dot"></span><div><div class="brand-name">Tierpraxolan</div><div class="brand-tag">Fachklinik für Kleintiere</div></div></div>
  <p class="abs eyebrow" style="left:41px;top:75px">Our Mission</p>
  <h2 class="abs display" style="left:41px;top:88px;font-size:12.5px;line-height:1.5">Supporting veterinary<br>practice success and<br>fostering fulfilling careers</h2>
  <p class="abs body-copy" style="left:41px;top:156px;width:202px">Lorem Ipsum is simply dummy text of the printing and typesetting industry. Lorem Ipsum has been the industry's standard dummy text ever since the 1500s, when an unknown printer took a galley of type and scrambled it to make a type specimen book. It has survived not only five centuries, but also the leap into electronic typesetting, remaining essentially unchanged. It was popularized in the 1960s with the release of Lettrafix sheets containing Lorem Ipsum passages, and more recently with desktop publishing software like Folio PageSetter including versions of Lorem Ipsum. It is a long-established fact that a reader will be distracted by the</p>
  <p class="footer-copy">© 2023 Tierpraxolan.</p><p class="footer-page">| 4</p>
</section>

<!-- 5 Media -->
<section class="slide col-l r3">
  <svg class="shapes" viewBox="0 0 542 304">
    <circle cx="341" cy="101" r="72" fill="url(#gXray)" role="img" aria-label="X-ray image of a small animal"/>
    <circle cx="341" cy="101" r="82" fill="none" stroke="var(--green)" stroke-width="4.5" stroke-linecap="round" pathLength="100" stroke-dasharray="33 67" transform="rotate(110 341 101)"/>
    <circle cx="196" cy="205" r="72" fill="url(#gSurgery)" role="img" aria-label="Photo: operating room with surgical equipment"/>
  </svg>
  <div class="brand" style="left:38px;top:16px"><span class="brand-dot"></span><div><div class="brand-name">Tierpraxolan</div><div class="brand-tag">Fachklinik für Kleintiere</div></div></div>
  <p class="abs body-copy" style="left:50px;top:62px;width:190px;text-align:right">Lorem Ipsum is simply dummy text of the printing and typesetting industry. Lorem Ipsum has been the industry's standard dummy text ever since the 1500s, when an unknown printer took a galley of type and scrambled it to make a type specimen book. It has survived not only five centuries, but also the leap into electronic typesetting.</p>
  <div class="pill" style="left:362px;top:40px;width:112px;background:var(--navy)">Service Lorem Ipsum is simply dummy text of the</div>
  <div class="pill" style="left:39px;top:145px;width:108px;background:var(--gold)">Service Lorem Ipsum is simply dummy text of the</div>
  <p class="abs body-copy" style="left:286px;top:195px;width:196px">Lorem Ipsum is simply dummy text of the printing and typesetting industry. Lorem Ipsum has been the industry's standard dummy text ever since the 1500s, when an unknown printer took a galley of type and scrambled it to make a type specimen book. It has survived not only five centuries, but also the leap into electronic typesetting.</p>
  <p class="footer-copy">© 2023 Tierpraxolan.</p><p class="footer-page">| 5</p>
</section>

<!-- 6 Bullets -->
<section class="slide col-r r3">
  <div class="brand" style="left:38px;top:16px"><span class="brand-dot"></span><div><div class="brand-name">Tierpraxolan</div><div class="brand-tag">Fachklinik für Kleintiere</div></div></div>
  <h2 class="abs display" style="left:41px;top:61px;font-size:12.5px;line-height:1.35">Text &amp; Four<br>Bullet Slide</h2>
  <p class="abs body-copy" style="left:41px;top:108px;width:186px">Lorem Ipsum is simply dummy text of the printing and typesetting industry. Lorem Ipsum has been the industry's standard dummy text ever since the 1500s, when an unknown printer took a galley of type and scrambled it to make a type specimen book. It has survived not only five centuries, but also the leap into electronic typesetting, remaining essentially unchanged. It was popularized in the 1960s with the release of Lettrafix sheets containing Lorem Ipsum passages, and more recently with desktop publishing software like Folio PageSetter including versions of Lorem Ipsum.<br><br>It is a long-established fact that a reader will be distracted by the readable content of a page when looking at its layout. The point of using Lorem Ipsum is that it has a more-or-less normal</p>
  <div class="bullet-icon" style="top:52px;background:var(--navy)"><svg width="16" height="16" viewBox="0 0 16 16" fill="none" stroke="#fff" stroke-width="1.3"><path d="M4 2v4a3 3 0 0 0 6 0V2"/><path d="M7 9v2a3 3 0 0 0 6 0V9"/><circle cx="13" cy="8" r="1.3"/></svg></div>
  <div class="bullet-icon" style="top:108px;background:var(--gold)"><svg width="16" height="16" viewBox="0 0 16 16" fill="none" stroke="#fff" stroke-width="1.3"><rect x="3" y="2.5" width="10" height="12" rx="1"/><path d="M6 2v2h4V2M5.5 7h5M5.5 9.5h5M5.5 12h3"/></svg></div>
  <div class="bullet-icon" style="top:164px;background:var(--rust)"><svg width="16" height="16" viewBox="0 0 16 16" fill="none" stroke="#fff" stroke-width="1.3"><rect x="4" y="5" width="8" height="9" rx="1.5"/><path d="M5 2.5h6v2.5H5zM8 7.5v4M6 9.5h4"/></svg></div>
  <div class="bullet-icon" style="top:221px;background:var(--green)"><svg width="16" height="16" viewBox="0 0 16 16" fill="none" stroke="#fff" stroke-width="1.3"><rect x="2" y="4.5" width="12" height="9" rx="1.5"/><path d="M6 4.5V3h4v1.5M8 7v4M6 9h4"/></svg></div>
  <div class="bullet" style="top:48px"><h4>Lorem ipsum is simply dummy</h4><p>Lorem Ipsum is simply dummy text of the printing and typesetting industry. Lorem Ipsum has been the industry's standard dummy text ever since the 1500s,</p></div>
  <div class="bullet" style="top:105px"><h4>Lorem ipsum is simply dummy</h4><p>Lorem Ipsum is simply dummy text of the printing and typesetting industry. Lorem Ipsum has been the industry's standard dummy text ever since the 1500s,</p></div>
  <div class="bullet" style="top:161px"><h4>Lorem ipsum is simply dummy</h4><p>Lorem Ipsum is simply dummy text of the printing and typesetting industry. Lorem Ipsum has been the industry's standard dummy text ever since the 1500s,</p></div>
  <div class="bullet" style="top:217px"><h4>Lorem ipsum is simply dummy</h4><p>Lorem Ipsum is simply dummy text of the printing and typesetting industry. Lorem Ipsum has been the industry's standard dummy text ever since the 1500s,</p></div>
  <p class="footer-copy" style="color:var(--gold)">© 2023 Tierpraxolan.</p><p class="footer-page" style="color:var(--gold)">| 6</p>
</section>

<!-- 7 Section: team -->
<section class="slide col-l r4 on-navy">
  <svg class="shapes" viewBox="0 0 542 304">
    <defs><clipPath id="clipTeamSplit"><circle cx="160" cy="152" r="108"/></clipPath></defs>
    <rect width="542" height="304" fill="var(--navy)"/>
    <g clip-path="url(#clipTeamSplit)">
      <polygon points="40,30 140,30 215,280 40,280" fill="url(#gGroup)" role="img" aria-label="Photo: clinic team group portrait"/>
      <polygon points="148,30 290,30 290,280 223,280" fill="url(#gDinner)" role="img" aria-label="Photo: team dinner at a long table"/>
    </g>
    <circle cx="160" cy="152" r="120" fill="none" stroke="var(--gold)" stroke-width="4.5" stroke-linecap="round" pathLength="100" stroke-dasharray="34 66" transform="rotate(125 160 152)"/>
    <circle cx="160" cy="152" r="120" fill="none" stroke="var(--green)" stroke-width="4.5" stroke-linecap="round" pathLength="100" stroke-dasharray="36 64" transform="rotate(-78 160 152)"/>
  </svg>
  <div class="brand on-dark" style="left:415px;top:16px"><span class="brand-dot"></span><div><div class="brand-name">Tierpraxolan</div><div class="brand-tag">Fachklinik für Kleintiere</div></div></div>
  <h2 class="abs display" style="left:325px;top:102px;font-size:24px;color:var(--white);line-height:1.5">Meet the<br>Tierpraxolan<br>Team</h2>
  <p class="footer-copy" style="color:var(--white)">© 2023 Tierpraxolan.</p><p class="footer-page">| 8</p>
</section>

<!-- 8 Team grid -->
<section class="slide col-r r4">
  <div class="brand" style="left:38px;top:16px"><span class="brand-dot"></span><div><div class="brand-name">Tierpraxolan</div><div class="brand-tag">Fachklinik für Kleintiere</div></div></div>
  <h2 class="abs display" style="left:0;width:542px;top:20px;text-align:center;font-size:12.5px">Tierpraxolan Team</h2>

  <div class="member" style="left:20px;top:62px"><svg width="72" height="72" viewBox="0 0 72 72"><circle cx="36" cy="36" r="29" fill="url(#gStaff)" role="img" aria-label="Team member portrait"/><circle cx="36" cy="36" r="34" fill="none" stroke="var(--gold)" stroke-width="2" pathLength="100" stroke-dasharray="35 65" transform="rotate(-40 36 36)"/><circle cx="36" cy="36" r="34" fill="none" stroke="var(--navy)" stroke-width="2" pathLength="100" stroke-dasharray="22 78" transform="rotate(190 36 36)"/></svg><p class="name">Dr. Lukas Brenner</p><p class="role">Diplomate ECVS, Spezialist für<br>Chirurgie Klinikleiter, Geschäftsführer</p></div>
  <div class="member" style="left:121px;top:62px"><svg width="72" height="72" viewBox="0 0 72 72"><circle cx="36" cy="36" r="29" fill="url(#gStaff)" role="img" aria-label="Team member portrait"/><circle cx="36" cy="36" r="34" fill="none" stroke="var(--gold)" stroke-width="2" pathLength="100" stroke-dasharray="35 65" transform="rotate(-40 36 36)"/><circle cx="36" cy="36" r="34" fill="none" stroke="var(--navy)" stroke-width="2" pathLength="100" stroke-dasharray="22 78" transform="rotate(190 36 36)"/></svg><p class="name">Dr. Lukas Brenner</p><p class="role">Diplomate ECVS, Spezialist für<br>Chirurgie Klinikleiter, Geschäftsführer</p></div>
  <div class="member" style="left:223px;top:62px"><svg width="72" height="72" viewBox="0 0 72 72"><circle cx="36" cy="36" r="29" fill="url(#gStaff)" role="img" aria-label="Team member portrait"/><circle cx="36" cy="36" r="34" fill="none" stroke="var(--gold)" stroke-width="2" pathLength="100" stroke-dasharray="35 65" transform="rotate(-40 36 36)"/><circle cx="36" cy="36" r="34" fill="none" stroke="var(--navy)" stroke-width="2" pathLength="100" stroke-dasharray="22 78" transform="rotate(190 36 36)"/></svg><p class="name">Dr. Lukas Brenner</p><p class="role">Diplomate ECVS, Spezialist für<br>Chirurgie Klinikleiter, Geschäftsführer</p></div>
  <div class="member" style="left:323px;top:62px"><svg width="72" height="72" viewBox="0 0 72 72"><circle cx="36" cy="36" r="29" fill="url(#gStaff)" role="img" aria-label="Team member portrait"/><circle cx="36" cy="36" r="34" fill="none" stroke="var(--gold)" stroke-width="2" pathLength="100" stroke-dasharray="35 65" transform="rotate(-40 36 36)"/><circle cx="36" cy="36" r="34" fill="none" stroke="var(--navy)" stroke-width="2" pathLength="100" stroke-dasharray="22 78" transform="rotate(190 36 36)"/></svg><p class="name">Dr. Lukas Brenner</p><p class="role">Diplomate ECVS, Spezialist für<br>Chirurgie Klinikleiter, Geschäftsführer</p></div>
  <div class="member" style="left:424px;top:62px"><svg width="72" height="72" viewBox="0 0 72 72"><circle cx="36" cy="36" r="29" fill="url(#gStaff)" role="img" aria-label="Team member portrait"/><circle cx="36" cy="36" r="34" fill="none" stroke="var(--gold)" stroke-width="2" pathLength="100" stroke-dasharray="35 65" transform="rotate(-40 36 36)"/><circle cx="36" cy="36" r="34" fill="none" stroke="var(--navy)" stroke-width="2" pathLength="100" stroke-dasharray="22 78" transform="rotate(190 36 36)"/></svg><p class="name">Dr. Lukas Brenner</p><p class="role">Diplomate ECVS, Spezialist für<br>Chirurgie Klinikleiter, Geschäftsführer</p></div>

  <div class="member" style="left:20px;top:167px"><svg width="72" height="72" viewBox="0 0 72 72"><circle cx="36" cy="36" r="29" fill="url(#gStaff)" role="img" aria-label="Team member portrait"/><circle cx="36" cy="36" r="34" fill="none" stroke="var(--gold)" stroke-width="2" pathLength="100" stroke-dasharray="35 65" transform="rotate(-40 36 36)"/><circle cx="36" cy="36" r="34" fill="none" stroke="var(--navy)" stroke-width="2" pathLength="100" stroke-dasharray="22 78" transform="rotate(190 36 36)"/></svg><p class="name">Dr. Lukas Brenner</p><p class="role">Diplomate ECVS, Spezialist für<br>Chirurgie Klinikleiter, Geschäftsführer</p></div>
  <div class="member" style="left:121px;top:167px"><svg width="72" height="72" viewBox="0 0 72 72"><circle cx="36" cy="36" r="29" fill="url(#gStaff)" role="img" aria-label="Team member portrait"/><circle cx="36" cy="36" r="34" fill="none" stroke="var(--gold)" stroke-width="2" pathLength="100" stroke-dasharray="35 65" transform="rotate(-40 36 36)"/><circle cx="36" cy="36" r="34" fill="none" stroke="var(--navy)" stroke-width="2" pathLength="100" stroke-dasharray="22 78" transform="rotate(190 36 36)"/></svg><p class="name">Dr. Lukas Brenner</p><p class="role">Diplomate ECVS, Spezialist für<br>Chirurgie Klinikleiter, Geschäftsführer</p></div>
  <div class="member" style="left:223px;top:167px"><svg width="72" height="72" viewBox="0 0 72 72"><circle cx="36" cy="36" r="29" fill="url(#gStaff)" role="img" aria-label="Team member portrait"/><circle cx="36" cy="36" r="34" fill="none" stroke="var(--gold)" stroke-width="2" pathLength="100" stroke-dasharray="35 65" transform="rotate(-40 36 36)"/><circle cx="36" cy="36" r="34" fill="none" stroke="var(--navy)" stroke-width="2" pathLength="100" stroke-dasharray="22 78" transform="rotate(190 36 36)"/></svg><p class="name">Dr. Lukas Brenner</p><p class="role">Diplomate ECVS, Spezialist für<br>Chirurgie Klinikleiter, Geschäftsführer</p></div>
  <div class="member" style="left:323px;top:167px"><svg width="72" height="72" viewBox="0 0 72 72"><circle cx="36" cy="36" r="29" fill="url(#gStaff)" role="img" aria-label="Team member portrait"/><circle cx="36" cy="36" r="34" fill="none" stroke="var(--gold)" stroke-width="2" pathLength="100" stroke-dasharray="35 65" transform="rotate(-40 36 36)"/><circle cx="36" cy="36" r="34" fill="none" stroke="var(--navy)" stroke-width="2" pathLength="100" stroke-dasharray="22 78" transform="rotate(190 36 36)"/></svg><p class="name">Dr. Lukas Brenner</p><p class="role">Diplomate ECVS, Spezialist für<br>Chirurgie Klinikleiter, Geschäftsführer</p></div>
  <div class="member" style="left:424px;top:167px"><svg width="72" height="72" viewBox="0 0 72 72"><circle cx="36" cy="36" r="29" fill="url(#gStaff)" role="img" aria-label="Team member portrait"/><circle cx="36" cy="36" r="34" fill="none" stroke="var(--gold)" stroke-width="2" pathLength="100" stroke-dasharray="35 65" transform="rotate(-40 36 36)"/><circle cx="36" cy="36" r="34" fill="none" stroke="var(--navy)" stroke-width="2" pathLength="100" stroke-dasharray="22 78" transform="rotate(190 36 36)"/></svg><p class="name">Dr. Lukas Brenner</p><p class="role">Diplomate ECVS, Spezialist für<br>Chirurgie Klinikleiter, Geschäftsführer</p></div>
  <p class="footer-copy">© 2023 Tierpraxolan.</p><p class="footer-page">| 9</p>
</section>

<!-- 9 Section: customers -->
<section class="slide col-l r5 on-navy">
  <svg class="shapes" viewBox="0 0 542 304">
    <defs><clipPath id="clipCustomerSplit"><circle cx="160" cy="152" r="108"/></clipPath></defs>
    <rect width="542" height="304" fill="var(--navy)"/>
    <g clip-path="url(#clipCustomerSplit)">
      <polygon points="40,30 140,30 215,280 40,280" fill="url(#gPortraitSoft)" role="img" aria-label="Photo: pet owner holding her dog"/>
      <polygon points="148,30 290,30 290,280 223,280" fill="url(#gWhiteDog)" role="img" aria-label="Photo: white terrier on the examination table"/>
    </g>
    <circle cx="160" cy="152" r="120" fill="none" stroke="var(--gold)" stroke-width="4.5" stroke-linecap="round" pathLength="100" stroke-dasharray="34 66" transform="rotate(125 160 152)"/>
    <circle cx="160" cy="152" r="120" fill="none" stroke="var(--rust)" stroke-width="4.5" stroke-linecap="round" pathLength="100" stroke-dasharray="36 64" transform="rotate(-78 160 152)"/>
  </svg>
  <div class="brand on-dark" style="left:415px;top:16px"><span class="brand-dot"></span><div><div class="brand-name">Tierpraxolan</div><div class="brand-tag">Fachklinik für Kleintiere</div></div></div>
  <h2 class="abs display" style="left:325px;top:84px;font-size:24px;color:var(--white);line-height:1.5">What Our<br>Customers<br>Say about<br>Tierpraxolan</h2>
  <p class="footer-copy" style="color:var(--white)">© 2023 Tierpraxolan.</p><p class="footer-page">| 10</p>
</section>

<!-- 10 Testimonials -->
<section class="slide col-r r5 on-navy">
  <svg class="shapes" viewBox="0 0 542 304">
    <path d="M0 270 C120 258 300 275 420 265 S520 255 542 250 L542 304 L0 304 Z" fill="var(--navy)"/>
  </svg>
  <div class="brand" style="left:38px;top:16px"><span class="brand-dot"></span><div><div class="brand-name">Tierpraxolan</div><div class="brand-tag">Fachklinik für Kleintiere</div></div></div>
  <h2 class="abs display" style="left:0;width:542px;top:20px;text-align:center;font-size:12.5px">What Our Customers Say</h2>
  <div class="quote" style="left:28px;top:72px"><svg width="76" height="76" viewBox="0 0 76 76" style="display:block;margin:0 auto"><circle cx="38" cy="38" r="31" fill="url(#gPortraitSoft)" role="img" aria-label="Customer portrait"/><circle cx="38" cy="38" r="35" fill="none" stroke="var(--gold)" stroke-width="2" pathLength="100" stroke-dasharray="30 70" transform="rotate(-30 38 38)"/><circle cx="38" cy="38" r="35" fill="none" stroke="var(--navy)" stroke-width="2" pathLength="100" stroke-dasharray="22 78" transform="rotate(190 38 38)"/></svg><p>Lorem ipsum dolor a yuim sit amet, consectetuer at rtge adipiscing elit. Maecenas porttitor congue massa. Fus ce pos uere, magna sed pulvinar ultricies, purus lectus males uada libero, s it amet commodo magna eros quis umapurus lectus males uada .</p><p class="who">Costumer Name</p></div>
  <div class="quote" style="left:201px;top:72px"><svg width="76" height="76" viewBox="0 0 76 76" style="display:block;margin:0 auto"><circle cx="38" cy="38" r="31" fill="url(#gPortraitSoft)" role="img" aria-label="Customer portrait"/><circle cx="38" cy="38" r="35" fill="none" stroke="var(--gold)" stroke-width="2" pathLength="100" stroke-dasharray="30 70" transform="rotate(-30 38 38)"/><circle cx="38" cy="38" r="35" fill="none" stroke="var(--navy)" stroke-width="2" pathLength="100" stroke-dasharray="22 78" transform="rotate(190 38 38)"/></svg><p>Lorem ipsum dolor a yuim sit amet, consectetuer at rtge adipiscing elit. Maecenas porttitor congue massa. Fus ce pos uere, magna sed pulvinar ultricies, purus lectus males uada libero, s it amet commodo magna eros quis uma purus lectus males uada .</p><p class="who">Costumer Name</p></div>
  <div class="quote" style="left:375px;top:72px"><svg width="76" height="76" viewBox="0 0 76 76" style="display:block;margin:0 auto"><circle cx="38" cy="38" r="31" fill="url(#gPortraitSoft)" role="img" aria-label="Customer portrait"/><circle cx="38" cy="38" r="35" fill="none" stroke="var(--gold)" stroke-width="2" pathLength="100" stroke-dasharray="30 70" transform="rotate(-30 38 38)"/><circle cx="38" cy="38" r="35" fill="none" stroke="var(--navy)" stroke-width="2" pathLength="100" stroke-dasharray="22 78" transform="rotate(190 38 38)"/></svg><p>Lorem ipsum dolor a yuim sit amet, consectetuer at rtge adipiscing elit. Maecenas porttitor congue massa. Fus ce pos uere, magna sed pulvinar ultricies, purus lectus males uada libero, s it amet commodo magna eros quis umapurus lectus males uada .</p><p class="who">Costumer Name</p></div>
  <p class="footer-copy" style="color:var(--gold)">© 2023 Tierpraxolan.</p><p class="footer-page">| 11</p>
</section>

<!-- 11 Practice owners -->
<section class="slide col-l r6">
  <svg class="shapes" viewBox="0 0 542 304">
    <rect x="0" y="47" width="320" height="209" fill="var(--navy)"/>
    <circle cx="364" cy="153" r="90" fill="url(#gScanner)" role="img" aria-label="Photo: veterinarian preparing a dog for a CT scan"/>
    <circle cx="364" cy="153" r="102" fill="none" stroke="var(--gold)" stroke-width="4.5" stroke-linecap="round" pathLength="100" stroke-dasharray="42 58" transform="rotate(105 364 153)"/>
    <circle cx="446" cy="149" r="43" fill="url(#gUltrasound)" stroke="var(--white)" stroke-width="2" role="img" aria-label="Photo: ultrasound examination"/>
    <circle cx="446" cy="149" r="53" fill="none" stroke="var(--navy)" stroke-width="4" stroke-linecap="round" pathLength="100" stroke-dasharray="26 74" transform="rotate(-30 446 149)"/>
  </svg>
  <div class="brand" style="left:38px;top:10px"><span class="brand-dot"></span><div><div class="brand-name">Tierpraxolan</div><div class="brand-tag">Fachklinik für Kleintiere</div></div></div>
  <p class="abs eyebrow" style="left:40px;top:70px;color:var(--white)">Practice Owners</p>
  <h2 class="abs display" style="left:39px;top:84px;font-size:12.8px;color:var(--white);line-height:1.5">Confidential Veterinary<br>Practice Valuations,<br>Seamless Transitions</h2>
  <p class="abs body-copy" style="left:38px;top:159px;width:180px;color:var(--white);text-align:left">Lorem Ipsum is simply dummy text of the printing and typesetting industry. Lorem Ipsum has been the industry's standard dummy text ever since the 1500s, when an unknown printer took a galley of type and scrambled it to make a type specimen book. It has survived not only five centuries, but also the leap into electronic typesetting, remaining essentially unchanged.</p>
  <p class="footer-copy">© 2023 Tierpraxolan.</p><p class="footer-page">| 7</p>
</section>

<!-- 12 Classic -->
<section class="slide col-r r6">
  <div class="brand" style="left:38px;top:16px"><span class="brand-dot"></span><div><div class="brand-name">Tierpraxolan</div><div class="brand-tag">Fachklinik für Kleintiere</div></div></div>
  <h2 class="abs display" style="left:152px;top:16px;font-size:15.5px">Classic Title &amp; Content silde</h2>
  <p class="abs col-head" style="left:41px;top:64px">What is Lorem Ipsum?</p>
  <p class="abs col-text" style="left:41px;top:92px;width:160px">Lorem Ipsum is simply dummy text of the printing and typesetting industry. Lorem Ipsum has been the industry's standard dummy text ever since the 1500s, when an unknown printer took a galley of type and scrambled it to make a type specimen book. It has survived not only five centuries, but also the leap into electronic typesetting, remaining essentially unchanged. It was popularised in the 1960s with the release of Lettrafix sheets containing Lorem Ipsum passages, and more recently with desktop publishing software like Folio PageSetter including versions of Lorem Ipsum.</p>
  <p class="abs col-head" style="left:251px;top:58px">Why do we use it?</p>
  <p class="abs col-text" style="left:251px;top:83px;width:254px">It is a long-established fact that a reader will be distracted by the readable content of a page when looking at its layout. The point of using Lorem Ipsum is that it has a more-or-less normal distribution of letters, as opposed to using 'Content here, content here', making it look like readable English. Many desktop publishing packages and web page editors now use Lorem Ipsum as their default model text, and a search for 'lorem ipsum' will uncover many web sites still in their infancy. Various versions have evolved over the years, sometimes by accident, sometimes on purpose (injected humor and the like).</p>
  <p class="abs col-head" style="left:251px;top:206px">Where does it come from?</p>
  <p class="abs col-text" style="left:251px;top:217px;width:254px">Contrary to popular belief, Lorem Ipsum is not simply random text. It has roots in a piece of classical Latin literature from 45 BC, making it over 2000 years old. Martin Keller, a Latin professor at Eastbrook College in Virginia, looked up one of the more obscure Latin words, consectetur</p>
  <p class="footer-copy">© 2023 Tierpraxolan.</p><p class="footer-page" style="color:var(--gold)">| 12</p>
</section>

</body>
</html>
```